Lead Sales Portal Needs to Generate B2B Signup's

We are looking for banner ad designs to drive new business (B2B) traffic to our insurance and mortgage industry self serve lead sites. The sites are HomeLoanProspectHub.com and PolicyProspectHub.com, and we service over 45,000 insurance agents and mortgage lenders in a self serve lead portal model. We want our banners to generate more of these clients.

Our clients come to our sites, browse our database and then pick out and purchase the consumer leads that they need to generate new business.

We advertise extensively on Zorvia and on other PPC platforms, and our existing banners are looking really tired.

Some of the ad copy that works well for us is:

Cherry Pick Your Life Leads - Why Pay More Than $3.50 For Life Insurance Leads?
Sign up today and we'll match up to $250

Agents - Here's $250 For New Clients. Cherry Pick Your Life Insurance Leads & Save! Sign up today and we'll match up to $250

One of our Landing Pages that performs well is here:
http://www.policyprospecthub.com/lp/008/

One of our competitors ad's are here:

http://www.adwatchery.com/search/results?q=RateBeacon&ad=518294

We're looking for a design that is eye catching, uses our "Deeply Discounted Leads" and our "$250 match bonus"

Target Market(s)

These are insurance agents and mortgage lenders. All of our clients are business' or individuals within the business. This is a B2B campaign,

Industry/Entity Type

Insurance

Requirements
Must have
• We must have the logos for the sites in the banners. Also, we must have a call to action arrow and "Go" button

One or two designs.

File type

.JPEG
.JPG
.PNG
.GIF

File size

150 KB or smaller

Image sizes

Vertical rectangle: 240 x 400
Mobile leaderboard: 320 x 50
Banner: 468 x 60
Leaderboard: 728 x 90
Square: 250 x 250
Small square: 200 x 200
Large rectangle: 336 x 280
Inline rectangle: 300 x 250
Skyscraper: 120 x 600
Wide skyscraper: 160 x 600
Half-page: 300 x 600
Large leaderboard: 970 x 90

```html
<!DOCTYPE html>
<html lang="en">
<head>
<meta charset="utf-8">
<title>Policy Prospect Hub – Banner Set</title>
<link rel="stylesheet" href="https://fonts.googleapis.com/css2?family=Oswald:wght@500;700&family=Roboto:wght@400;700&display=swap">
<style>
  :root {
    --stage: #e6e6e6;
    --ink: #1b1b1b;
    --red: #b5121b;
    --white: #ffffff;
    --panel-dark: #262626;
    --bar-dark: #2b2b2b;
    --edge-grey: #c9c9c9;
    --btn-top: #ffd21a;
    --btn-bottom: #f6a800;
    --btn-text: #1a1a1a;
    --photo-light: #d9d6d2;
    --photo-mid: #8b8580;
    --photo-dark: #2a2a2c;
  }
  * { box-sizing: border-box; margin: 0; padding: 0; }
  html, body { width: 1200px; height: 596px; overflow: hidden; }
  body { background: var(--stage); position: relative; font-family: "Oswald", "Arial Narrow", sans-serif; }

  .banner { position: absolute; top: 88px; width: 504px; height: 420px; overflow: hidden; box-shadow: 0 6px 18px rgba(0,0,0,.25); }
  .banner--light { left: 80px; background: var(--white); }
  .banner--dark { left: 616px; background: var(--white); }

  .photo { position: absolute; background: linear-gradient(160deg, var(--photo-light) 0%, var(--photo-mid) 45%, var(--photo-dark) 100%); }
  .banner--light .photo { left: 150px; top: 0; width: 354px; height: 342px; }
  .banner--dark .photo { left: 230px; top: 0; width: 274px; height: 347px; }

  .copy-panel { position: absolute; left: 0; top: 0; width: 228px; height: 339px; background: var(--white); border-bottom-right-radius: 30px; }
  .line { position: absolute; left: 22px; font-weight: 700; text-transform: uppercase; line-height: 1; white-space: nowrap; letter-spacing: -0.5px; }
  .line--ink { color: var(--ink); }
  .line--red { color: var(--red); }
  .line--white { color: var(--white); }
  .rule { position: absolute; left: 22px; width: 188px; height: 2px; background: #bdbdbd; }

  .bottom-bar { position: absolute; left: 0; top: 342px; width: 504px; height: 78px; background: var(--bar-dark); border-top: 4px solid #9a9a9a; }
  .brand { position: absolute; display: flex; align-items: center; gap: 10px; font-family: "Roboto", sans-serif; font-weight: 400; font-size: 24px; white-space: nowrap; }
  .brand__dot { width: 38px; height: 38px; border-radius: 50%; flex: none; }
  .banner--light .brand { left: 10px; top: 18px; color: var(--white); }
  .banner--light .brand__dot { background: var(--white); }
  .banner--dark .brand { color: var(--ink); }
  .banner--dark .brand__dot { background: var(--ink); }

  .cta { position: absolute; display: flex; align-items: center; justify-content: center; gap: 10px; border-radius: 6px; background: linear-gradient(var(--btn-top), var(--btn-bottom)); border: 1px solid #c98a00; font-family: "Roboto", sans-serif; font-weight: 700; font-size: 21px; color: var(--btn-text); white-space: nowrap; }
  .cta svg { width: 30px; height: 30px; }
  .banner--light .cta { left: 300px; top: 14px; width: 188px; height: 46px; }
  .banner--dark .cta { left: 10px; top: 246px; width: 192px; height: 46px; }

  .chevron { position: absolute; left: 0; top: 0; width: 270px; height: 420px; }
  .logo-bar { position: absolute; left: 232px; top: 347px; width: 272px; height: 73px; background: var(--white); }
  .logo-bar .brand { left: 14px; top: 19px; gap: 8px; font-size: 21px; }
  .logo-bar .brand__dot { width: 32px; height: 32px; }
</style>
</head>
<body>

  <!-- Large rectangle, light variant -->
  <section class="banner banner--light">
    <div class="photo" role="img" aria-label="Photo of two smiling young business professionals in dark suits"></div>
    <div class="copy-panel">
      <div class="line line--ink" style="top:12px;font-size:33px;">Pick your life</div>
      <div class="line line--red" style="top:48px;font-size:42px;">Insurance</div>
      <div class="line line--ink" style="top:92px;font-size:54px;">Leads &amp;</div>
      <div class="line line--ink" style="top:140px;font-size:86px;">Save!</div>
      <div class="rule" style="top:236px;"></div>
      <div class="line line--ink" style="top:246px;font-size:35px;">We'll match</div>
      <div class="line line--red" style="top:284px;font-size:40px;">Up to $250</div>
    </div>
    <div class="bottom-bar">
      <div class="brand"><span class="brand__dot"></span>Policy Prospect Hub</div>
      <div class="cta">Sign up Now!
        <svg viewBox="0 0 30 30"><circle cx="15" cy="15" r="14" fill="#1f1f1f"/><path d="M12 8l8 7-8 7" fill="none" stroke="#fff" stroke-width="3.5" stroke-linecap="round" stroke-linejoin="round"/></svg>
      </div>
    </div>
  </section>

  <!-- Large rectangle, dark variant -->
  <section class="banner banner--dark">
    <div class="photo" role="img" aria-label="Photo of two smiling young business professionals in dark suits"></div>
    <svg class="chevron" viewBox="0 0 270 420" aria-hidden="true">
      <polygon points="0,0 232,0 268,178 232,420 0,420" fill="var(--edge-grey)"/>
      <polygon points="0,0 222,0 258,178 222,420 0,420" fill="var(--panel-dark)"/>
    </svg>
    <div class="line line--white" style="top:22px;left:18px;font-size:33px;">Pick your life</div>
    <div class="line line--white" style="top:58px;left:18px;font-size:44px;">Insurance</div>
    <div class="line line--white" style="top:104px;left:18px;font-size:58px;">Leads &amp;</div>
    <div class="line line--white" style="top:158px;left:18px;font-size:80px;">Save!</div>
    <div class="cta">Sign up Now!
      <svg viewBox="0 0 30 30"><circle cx="15" cy="15" r="14" fill="#1f1f1f"/><path d="M12 8l8 7-8 7" fill="none" stroke="#fff" stroke-width="3.5" stroke-linecap="round" stroke-linejoin="round"/></svg>
    </div>
    <div class="line line--white" style="top:308px;left:18px;font-size:37px;">We'll match</div>
    <div class="line line--white" style="top:348px;left:18px;font-size:40px;">Up to $250</div>
    <div class="logo-bar">
      <div class="brand"><span class="brand__dot"></span>Policy Prospect Hub</div>
    </div>
  </section>

</body>
</html>
```